Creative Website Design for Post Production Sound Editorial Company

We are seeking a highly creative and talented web designer to lead the transformation of our existing website into a visually captivating and user-friendly online platform for our Post Production Sound Editorial Company. As a specialized provider of sound editing services for diverse media productions, we recognize the critical importance of a compelling online presence that reflects our expertise and brand identity.
Project Overview:
Our website is already active and hosted via WordPress at https://pagecrate.example/view/velmortaudiocraft.example. Note: The brand book is in the guide. While it serves as a foundation, we are committed to elevating its impact by entrusting you with the task of enhancing its design, functionality, and user experience.

Target Market(s)

* Film Producers: Producers involved in film production, including directors, executive producers, and independent filmmakers, who require high-quality sound editing services to enhance their cinematic projects. * Television Producers: Producers responsible for television shows, series, and documentaries seeking post-production sound editing expertise to improve the audio quality of their content. * Podcast Producers: Podcast creators and producers in need of sound editorial services to enhance the audio experience and professionalism of their podcasts. * Advertising Agencies: Agencies working on multimedia advertising campaigns that require sound editing for commercials, promotional videos, and branded content. * Corporate Video Producers: Professionals responsible for producing corporate videos, training materials, and presentations that require polished and clear audio. * Documentary Filmmakers: Filmmakers creating documentary films who require sound editing to improve the audio clarity and storytelling impact of their projects. * Online Content Creators: Influencers, vloggers, and content creators producing online videos and multimedia content looking to enhance the audio quality of their productions. * Post-Production Studios: Post-production studios that may require specialized sound editing services for their clients, such as major film studios and media companies. * Event Planners: Event planners and organizers who need sound editing for event recordings, promotional videos, and multimedia presentations. * Educational Institutions: Educational institutions, including universities and schools, seeking sound editing services for educational videos, e-learning materials, and multimedia resources. * Government and Nonprofit Organizations: Government agencies and nonprofit organizations in need of sound editing services for public service announcements, informational videos, and awareness campaigns. * Streaming Platforms: Streaming platforms and online content distribution channels that require high-quality sound editing for their content libraries.

Industry/Entity Type

"Media and Entertainment." "Post-Production Services" or "Audio Post-Production Services."

Coding

Coded - Design and coding required

Number of Pages Required

5+ page

Font styles to use
Other font styles liked:
• Nexa

Colors

Designer to choose only greyscale colors for use in the design.

Requirements
Must have
• * Clean and Modern Design: Use a clean and contemporary design with a minimalist aesthetic. This will convey professionalism and make it easy for visitors to navigate our site. * High-Quality Imagery and Multimedia: Incorporate high-resolution images, video clips, and audio samples that showcase our work and expertise. Visual and auditory elements are essential in the sound editing industry. * Color Palette: Use Branding Kit for the color palette * Typography: Use Branding Kit (Nexa) to select clear, legible fonts for easy reading. * Responsive Design: Ensure that the website is fully responsive, adapting seamlessly to various screen sizes and devices. This is crucial for user-friendliness and accessibility. * Intuitive Navigation: Design a user-friendly navigation menu with clear headings and categories. Users should easily find information about our services, portfolio, about the company, and contact details. * Video Backgrounds: Consider using video backgrounds on the homepage or specific sections to capture attention and highlight our expertise. Ensure that the videos are relevant to our services. * Testimonials and Case Studies: Include client testimonials and case studies to build trust and credibility. Showcase successful projects we've worked on and the positive impact our sound editing services have had. * Interactive Elements: Incorporate interactive elements such as buttons, hover effects, and animations to engage visitors and make the website more dynamic. * Call-to-Action (CTA) Buttons: Strategically place CTA buttons throughout the site to encourage visitors to get in touch, request a quote, or explore our portfolio. * Contact Information: Make it easy for visitors to contact us by placing clear contact information, including a contact form, phone number, and email address. * Social Media Integration: Connect your social media profiles to the website to foster engagement and allow visitors to follow your updates. * Accessibility Features: Ensure that the website is accessible to all users, including those with disabilities. This includes using alt text for images and ensuring keyboard navigation is smooth. * Loading Speed: Optimize the website's loading speed to provide a seamless browsing experience. * Security: Implement security measures to protect user data and maintain trust.
Nice to have
• * Testimonials and Case Studies: Include client testimonials and case studies to build trust and credibility. Showcase successful projects you've worked on and the positive impact your sound editing services have had. * Blog Section: Include a blog section where you can share industry insights, tips, and updates. This can position your company as an authority in sound editing.
Should not have
• designers who are inexperienced

```html
<!DOCTYPE html>
<html lang="en">
<head>
<meta charset="utf-8">
<title>Velmort Audiocraft — Website Concept</title>
<link href="https://fonts.googleapis.com/css2?family=Outfit:wght@300;400;500;600;700&display=swap" rel="stylesheet">
<style>
:root{
  --stage:#141414;
  --ink:#111111;
  --paper:#ffffff;
  --light-a:#dadada;
  --light-b:#bcbcbc;
  --dark-a:#2f2f2f;
  --dark-b:#393939;
  --card-dark:#3d3d3d;
}
*{margin:0;padding:0;box-sizing:border-box}
html,body{width:1200px;height:4080px;overflow:hidden}
body{background:var(--stage);font-family:"Outfit",sans-serif;position:relative;color:var(--ink)}

.masthead{position:absolute;left:253px;top:76px;display:flex;align-items:center;gap:28px}
.masthead__mark{width:164px;height:164px;border-radius:50%;border:5px solid #d9d9d9;background:#5e5e5e}
.masthead__name{font-size:52px;font-weight:600;color:var(--paper);letter-spacing:-0.5px}

.panel{position:absolute;left:139px;width:922px;height:518px;overflow:hidden}
.panel--light{background:linear-gradient(120deg,var(--light-a),var(--light-b));color:var(--ink)}
.panel--dark{background:linear-gradient(120deg,var(--dark-a),var(--dark-b));color:var(--paper)}

.brand{position:absolute;left:84px;top:38px;display:flex;align-items:center;gap:10px;font-size:17px;font-weight:600}
.brand__mark{width:46px;height:46px;border-radius:50%;border:2px solid currentColor;opacity:.7}

.connect{position:absolute;left:800px;top:0;width:122px;height:122px}

.nav{position:absolute;right:44px;top:162px;width:160px;height:284px;border-right:2px solid #8a8a8a;list-style:none}
.panel--dark .nav{border-right-color:#6a6a6a}
.nav li{position:absolute;right:20px;font-size:9px;font-weight:500;letter-spacing:.3px;text-transform:uppercase}
.nav li.is-active{font-weight:700}
.nav li.is-active::after{content:"";position:absolute;right:-22px;top:-10px;width:3px;height:30px;background:currentColor}
.nav li:nth-child(1){top:16px}.nav li:nth-child(2){top:66px}.nav li:nth-child(3){top:116px}
.nav li:nth-child(4){top:165px}.nav li:nth-child(5){top:216px}.nav li:nth-child(6){top:265px}

.eyebrow{font-size:14px;font-weight:400}
.headline{font-size:31px;font-weight:400;line-height:1.05;letter-spacing:-.3px}
.body-copy{font-size:8px;line-height:1.75;font-weight:300}
.btn{display:inline-flex;align-items:center;justify-content:center;gap:14px;height:23px;width:108px;border-radius:3px;font-size:7px;font-weight:500}
.btn--dark{background:#333;color:var(--paper)}
.btn--light{background:var(--paper);color:var(--ink)}

/* hero */
.hero__text{position:absolute;left:152px;top:168px;width:270px}
.hero__text .headline{margin-top:6px}
.hero__text .body-copy{margin-top:12px;color:#444}
.hero__text .btn{margin-top:18px}
.socials{position:absolute;left:146px;top:425px;display:flex;gap:18px}
.socials span{width:19px;height:19px;border-radius:50%;background:#555}
.hero__media{position:absolute;left:451px;top:119px;width:300px;height:300px;border-radius:50%;background:radial-gradient(circle at 50% 50%,#4a4a4a 0,#5a5a5a 40%,#a8a8a8 72%,rgba(190,190,190,0) 100%);display:flex;align-items:center;justify-content:center}
.hero__play{width:36px;height:36px}

/* about */
.about__photo{position:absolute;left:82px;top:122px;width:331px;height:336px;border-radius:4px;background:linear-gradient(135deg,#1a1a1a,#6b6b6b 60%,#2a2a2a)}
.about__text{position:absolute;left:446px;top:150px;width:300px}
.about__text .headline{margin-top:8px}
.about__text .body-copy{margin-top:12px;color:#cfcfcf}
.about__text .btn{margin-top:18px}

/* centered header */
.center-head{position:absolute;left:0;width:922px;text-align:center}
.center-head .eyebrow{font-size:13px}
.center-head .headline{margin-top:6px}

/* showreel */
.reel{position:absolute;left:150px;top:218px;display:flex;gap:14px}
.reel__item{width:198px;text-align:center}
.reel__poster{height:146px;border-radius:4px;background:linear-gradient(160deg,#2a2a2a,#8a8a8a 55%,#3a3a3a)}
.reel__title{margin-top:11px;font-size:15px;font-weight:400}

/* services */
.services{position:absolute;left:150px;top:253px;display:flex;gap:14px}
.service{width:144px;height:117px;border-radius:3px;background:var(--paper);color:var(--ink);display:flex;flex-direction:column;align-items:center;justify-content:center;gap:10px;font-size:10px}
.service--active{background:var(--card-dark);color:var(--paper);box-shadow:0 2px 8px rgba(0,0,0,.3)}
.service svg{width:38px;height:38px}

/* testimonials */
.testi__head{position:absolute;left:152px;top:128px}
.testi__head .eyebrow{font-size:13px}
.testi__head .headline{margin-top:4px}
.quote{position:absolute;left:154px;top:230px;width:278px;height:170px;background:#3a3a3a;color:var(--paper);border-radius:3px;padding:34px 28px 0 28px}
.quote p{font-size:8px;line-height:1.7;font-weight:300}
.quote .stars{margin-top:14px;font-size:8px;letter-spacing:1px}
.quote .who{font-size:8px;font-weight:700;margin-top:3px}
.avatar{position:absolute;left:357px;top:367px;width:48px;height:48px;border-radius:50%;border:2px solid var(--paper);background:linear-gradient(160deg,#7a7a7a,#2c2c2c)}
.dots{position:absolute;left:162px;top:418px;width:66px;height:10px}
.globe{position:absolute;left:520px;top:200px;width:330px;height:330px;border-radius:50%;background:radial-gradient(circle at 40% 40%,#f2f2f2,#bdbdbd 70%,#9a9a9a)}

/* contact */
.contact__text{position:absolute;left:160px;top:112px;width:602px;text-align:center}
.contact__text .eyebrow{font-size:13px}
.contact__text .headline{margin-top:6px}
.contact__text .body-copy{margin-top:10px;color:#cfcfcf}
.contact__text .btn{margin-top:16px}
.footer{position:absolute;left:0;top:336px;width:922px;height:182px;border-top:1px solid #444;background:#303030}
.footer__brand{position:absolute;left:146px;top:20px;display:flex;align-items:center;gap:8px;font-size:13px;font-weight:600}
.footer__brand span{width:34px;height:34px;border-radius:50%;border:2px solid currentColor;opacity:.7}
.footer__about{position:absolute;left:148px;top:70px;width:165px;font-size:8px;line-height:1.75;color:#cfcfcf}
.footer__links{position:absolute;left:378px;top:70px;width:190px;height:76px;border-left:1px solid #666;border-right:1px solid #666;list-style:none;text-align:center;font-size:8px;line-height:1.75;color:#cfcfcf}
.footer__legal{position:absolute;left:641px;top:86px;width:140px;font-size:8px;line-height:1.75;color:#cfcfcf}
</style>
</head>
<body>

<header class="masthead">
  <div class="masthead__mark"></div>
  <div class="masthead__name">Velmort Audiocraft</div>
</header>

<!-- Home -->
<section class="panel panel--light" style="top:351px">
  <div class="brand"><span class="brand__mark"></span>Velmort Audiocraft</div>
  <svg class="connect" viewBox="0 0 122 122" fill="none" stroke="#222">
    <path id="arcA" d="M14 10 A42 42 0 0 0 78 72" stroke="none"/>
    <text font-size="9" font-weight="600" letter-spacing="2" fill="#222" stroke="none"><textPath href="#arcA">CONNECT US</textPath></text>
    <path d="M104 28 L76 56 M84 28 H104 V48" stroke-width="1.2"/>
    <path d="M122 62 A40 40 0 0 1 84 84" stroke-width="1"/>
  </svg>
  <ul class="nav"><li class="is-active">Home</li><li>About</li><li>Our Work</li><li>Services</li><li>Testimonials</li><li>Contact</li></ul>

  <div class="hero__text">
    <div class="eyebrow">Bringing Your Story to</div>
    <h1 class="headline">Life Through the<br>Power of Sound</h1>
    <p class="body-copy">Welcome to Velmort Audiocraft, the premier destination for post-production sound editing services. With over 20 years of experience in the industry, our owner brings a wealth of expertise and knowledge to every project.</p>
    <div class="btn btn--dark">Play Video <svg width="9" height="10" viewBox="0 0 9 10"><path d="M0 0L9 5L0 10Z" fill="#fff"/></svg></div>
  </div>
  <div class="socials"><span></span><span></span><span></span></div>

  <div class="hero__media" role="img" aria-label="Showreel video still of a sound editor at a mixing desk, framed by an audio visualiser">
    <svg class="hero__play" viewBox="0 0 36 36"><path d="M8 4 L32 18 L8 32 Z" fill="#fff"/></svg>
  </div>
</section>

<!-- About -->
<section class="panel panel--dark" style="top:940px">
  <div class="brand"><span class="brand__mark"></span>Velmort Audiocraft</div>
  <svg class="connect" viewBox="0 0 122 122" fill="none" stroke="#fff">
    <path id="arcB" d="M14 10 A42 42 0 0 0 78 72" stroke="none"/>
    <text font-size="9" font-weight="600" letter-spacing="2" fill="#fff" stroke="none"><textPath href="#arcB">CONNECT US</textPath></text>
    <path d="M104 28 L76 56 M84 28 H104 V48" stroke-width="1.2"/>
    <path d="M122 62 A40 40 0 0 1 84 84" stroke-width="1"/>
  </svg>
  <ul class="nav"><li>Home</li><li class="is-active">About</li><li>Our Work</li><li>Services</li><li>Testimonials</li><li>Contact</li></ul>

  <div class="about__photo" role="img" aria-label="Engineer in headphones at a mixing console in a studio"></div>
  <div class="about__text">
    <div class="eyebrow">Our Sonic Odyssey</div>
    <h2 class="headline">Unveiling the Artistry<br>Behind the Sound</h2>
    <p class="body-copy">Embark on an unforgettable sonic odyssey as we unveil the artistry behind the sound at Velmort Audiocraft. With over 20 years of experience in post-production sound editing, our dedicated team brings expertise, creativity, and a deep understanding of the power of sound to enhance visual storytelling. We are passionate about pushing boundaries, exploring new sonic territories, and crafting immersive audio experiences that captivate audiences. Join us on this sonic adventure as we unravel the secrets behind the art of sound.</p>
    <div class="btn btn--light">See More</div>
  </div>
</section>

<!-- Our Work -->
<section class="panel panel--light" style="top:1553px">
  <div class="brand"><span class="brand__mark"></span>Velmort Audiocraft</div>
  <svg class="connect" viewBox="0 0 122 122" fill="none" stroke="#222">
    <path id="arcC" d="M14 10 A42 42 0 0 0 78 72" stroke="none"/>
    <text font-size="9" font-weight="600" letter-spacing="2" fill="#222" stroke="none"><textPath href="#arcC">CONNECT US</textPath></text>
    <path d="M104 28 L76 56 M84 28 H104 V48" stroke-width="1.2"/>
    <path d="M122 62 A40 40 0 0 1 84 84" stroke-width="1"/>
  </svg>
  <ul class="nav"><li>Home</li><li>About</li><li class="is-active">Our Work</li><li>Services</li><li>Testimonials</li><li>Contact</li></ul>

  <div class="center-head" style="top:102px">
    <div class="eyebrow">Sonic Showreel</div>
    <h2 class="headline">Where Creativity<br>Finds its Sonic Voice</h2>
  </div>
  <div class="reel">
    <div class="reel__item"><div class="reel__poster" role="img" aria-label="Film poster"></div><div class="reel__title">Lanterns Of Kiru</div></div>
    <div class="reel__item"><div class="reel__poster" role="img" aria-label="Film poster"></div><div class="reel__title">Quiet Hours</div></div>
    <div class="reel__item"><div class="reel__poster" role="img" aria-label="Series poster collage"></div><div class="reel__title">The Outlands</div></div>
  </div>
  <div class="btn btn--dark" style="position:absolute;left:407px;top:419px">See More</div>
</section>

<!-- Services -->
<section class="panel panel--dark" style="top:2172px">
  <div class="brand"><span class="brand__mark"></span>Velmort Audiocraft</div>
  <svg class="connect" viewBox="0 0 122 122" fill="none" stroke="#fff">
    <path id="arcD" d="M14 10 A42 42 0 0 0 78 72" stroke="none"/>
    <text font-size="9" font-weight="600" letter-spacing="2" fill="#fff" stroke="none"><textPath href="#arcD">CONNECT US</textPath></text>
    <path d="M104 28 L76 56 M84 28 H104 V48" stroke-width="1.2"/>
    <path d="M122 62 A40 40 0 0 1 84 84" stroke-width="1"/>
  </svg>
  <ul class="nav"><li>Home</li><li>About</li><li>Our Work</li><li class="is-active">Services</li><li>Testimonials</li><li>Contact</li></ul>

  <div class="center-head" style="top:126px">
    <div class="eyebrow">Sonic Alchemy</div>
    <h2 class="headline">Transforming Sound into<br>Captivating Experiences</h2>
  </div>
  <div class="services">
    <div class="service">
      <svg viewBox="0 0 38 38" fill="#222"><rect x="2" y="3" width="16" height="11" rx="2"/><rect x="20" y="6" width="16" height="11" rx="2"/><circle cx="10" cy="22" r="4"/><circle cx="28" cy="22" r="4"/><rect x="4" y="28" width="12" height="8" rx="3"/><rect x="22" y="28" width="12" height="8" rx="3"/></svg>
      Dialogue Editing
    </div>
    <div class="service service--active">
      <svg viewBox="0 0 38 38" stroke="#ddd" stroke-width="2" stroke-linecap="round"><path d="M5 17v4M9 14v10M13 16v6M17 10v18M21 13v12M25 16v6M29 14v10M33 17v4"/></svg>
      Sound Effects Editing
    </div>
    <div class="service">
      <svg viewBox="0 0 38 38" fill="none" stroke="#222" stroke-width="2"><rect x="3" y="3" width="32" height="32" rx="3"/><path d="M12 8v22M19 8v22M26 8v22"/><rect x="9" y="12" width="6" height="4" fill="#222"/><rect x="16" y="21" width="6" height="4" fill="#222"/><rect x="23" y="15" width="6" height="4" fill="#222"/></svg>
      foley editing
    </div>
    <div class="service">
      <svg viewBox="0 0 38 38" fill="none" stroke="#222" stroke-width="2"><rect x="3" y="6" width="32" height="26" rx="4"/><circle cx="13" cy="17" r="5"/><circle cx="25" cy="17" r="5"/><path d="M8 27h22"/></svg>
      ADR Editing And Mixing
    </div>
  </div>
  <div class="btn btn--light" style="position:absolute;left:407px;top:419px">See More</div>
</section>

<!-- Testimonials -->
<section class="panel panel--light" style="top:2791px;background:linear-gradient(120deg,#d2d2d2,#ececec)">
  <div class="brand"><span class="brand__mark"></span>Velmort Audiocraft</div>
  <svg class="connect" viewBox="0 0 122 122" fill="none" stroke="#222">
    <path id="arcE" d="M14 10 A42 42 0 0 0 78 72" stroke="none"/>
    <text font-size="9" font-weight="600" letter-spacing="2" fill="#222" stroke="none"><textPath href="#arcE">CONNECT US</textPath></text>
    <path d="M104 28 L76 56 M84 28 H104 V48" stroke-width="1.2"/>
    <path d="M122 62 A40 40 0 0 1 84 84" stroke-width="1"/>
  </svg>
  <div class="globe" role="img" aria-label="Dotted world globe with connection lines"></div>
  <ul class="nav"><li>Home</li><li>About</li><li>Our Work</li><li>Services</li><li class="is-active">Testimonials</li><li>Contact</li></ul>

  <div class="testi__head">
    <div class="eyebrow">Our Testimonials</div>
    <h2 class="headline">What Our Client Says</h2>
  </div>
  <div class="quote">
    <p>Lorem Ipsum is simply dummy text of the printing and typesetting industry. Lorem Ipsum has been the industry's standard dummy text ever since the 1500s, when an unknown printer took a galley of type and scrambled</p>
    <div class="stars">★★★★★</div>
    <div class="who">ELIAN - MD</div>
  </div>
  <div class="avatar" role="img" aria-label="Client portrait"></div>
  <svg class="dots" viewBox="0 0 66 10"><line x1="5" y1="5" x2="61" y2="5" stroke="#333"/><circle cx="5" cy="5" r="4" fill="#333"/><circle cx="33" cy="5" r="3" fill="#333"/><circle cx="61" cy="5" r="3" fill="#333"/></svg>
</section>

<!-- Contact -->
<section class="panel panel--dark" style="top:3429px">
  <div class="brand"><span class="brand__mark"></span>Velmort Audiocraft</div>
  <svg class="connect" viewBox="0 0 122 122" fill="none" stroke="#fff">
    <path id="arcF" d="M14 10 A42 42 0 0 0 78 72" stroke="none"/>
    <text font-size="9" font-weight="600" letter-spacing="2" fill="#fff" stroke="none"><textPath href="#arcF">CONNECT US</textPath></text>
    <path d="M104 28 L76 56 M84 28 H104 V48" stroke-width="1.2"/>
    <path d="M122 62 A40 40 0 0 1 84 84" stroke-width="1"/>
  </svg>

  <div class="contact__text">
    <div class="eyebrow">Sonic Connection</div>
    <h2 class="headline">Let's Craft Sonic Magic<br>Together</h2>
    <p class="body-copy">We believe in the power of collaboration and the magic that can be created when passionate individuals come together. Get in touch with our team at Velmort Audiocraft and let's embark on a sonic journey together. Whether you're a filmmaker, or any creative professional seeking to elevate your project with outstanding sound, we are here to listen, understand your vision, and bring it to life through our expertise in post-production sound editing.</p>
    <div class="btn btn--light">Contact Us</div>
  </div>

  <footer class="footer">
    <div class="footer__brand"><span></span>Velmort Audiocraft</div>
    <p class="footer__about">Let's collaborate and craft sonic magic that will captivate and resonate with your audience. Reach out to us today and let the sonic adventure begin.</p>
    <ul class="footer__links"><li>Home</li><li>About</li><li>Our Work</li><li>Services</li><li>Contact Us</li></ul>
    <p class="footer__legal">© 2023 Velmort Audiocraft All rights reserved Terms and Privacy Policy</p>
  </footer>
  <ul class="nav"><li>Home</li><li>About</li><li>Our Work</li><li>Services</li><li>Testimonials</li><li class="is-active">Contact</li></ul>
</section>

</body>
</html>
```